New exciting tequila brand needs fun and attention drawing bottle label.

We need a design for on the glass bottle for a new tequila brand called "Mango Spin Tequila". It can be a label, or the decoration for the entire bottle.
The brand is called "Mango Spin" and is targeting a young party crowd.
I would like the visual to play with the image of a "tiger" & the idea of "up"side down.
In a bar the bottle needs to stand out, so it can be a very colourful design.

Good luck

Target Market(s)

young party crowd

Industry/Entity Type

Crowd

Colors
ec2027
fbed22
f37123
ffffff
f8ba93
fbf289

Requirements
Must have
• tiger
Nice to have
• play with the idea of upside down
Should not have
• have seen it before feeling

```html
<!DOCTYPE html>
<html lang="en">
<head>
<meta charset="utf-8">
<title>Mango Spin Tequila – Bottle Label</title>
<link rel="stylesheet" href="https://fonts.googleapis.com/css2?family=Alfa+Slab+One&family=Italianno&family=Arimo&display=swap">
<style>
  :root {
    --label-black: #000000;
    --brand-yellow: #fbed22;
    --brand-orange: #f37123;
    --brand-peach: #f8ba93;
    --brand-cream: #fbf289;
    --brand-red: #ec2027;
    --rule-copper: #c9794a;
    --page-white: #ffffff;
  }
  html, body {
    margin: 0;
    padding: 0;
    width: 1200px;
    height: 1000px;
    overflow: hidden;
    background: var(--page-white);
  }
  .label {
    position: relative;
    width: 1200px;
    height: 1000px;
  }
  .label-frame {
    position: absolute;
    inset: 0;
  }
  .crest-ornament {
    position: absolute;
    left: 432px;
    top: 122px;
    width: 308px;
    height: 38px;
    background: linear-gradient(90deg, transparent, var(--brand-yellow) 20%, var(--brand-yellow) 80%, transparent);
    opacity: 0.55;
    border-radius: 19px;
  }
  .brand-name {
    position: absolute;
    left: 0;
    width: 1200px;
    top: 168px;
    margin: 0;
    text-align: center;
    font-family: "Alfa Slab One", serif;
    font-weight: 400;
    font-size: 128px;
    line-height: 170px;
    color: var(--brand-yellow);
    letter-spacing: 2px;
  }
  .registered-mark {
    position: absolute;
    left: 1040px;
    top: 172px;
    font-family: "Arimo", sans-serif;
    font-size: 26px;
    color: var(--brand-yellow);
  }
  .tagline-rule {
    position: absolute;
    left: 506px;
    width: 186px;
    height: 7px;
    border-top: 1.5px solid var(--rule-copper);
    border-bottom: 1.5px solid var(--rule-copper);
    box-sizing: border-box;
  }
  .tagline-rule.top { top: 364px; }
  .tagline-rule.bottom { top: 426px; }
  .tagline {
    position: absolute;
    left: 0;
    width: 1200px;
    top: 376px;
    margin: 0;
    text-align: center;
    font-family: "Italianno", cursive;
    font-size: 34px;
    line-height: 44px;
    color: var(--brand-yellow);
    letter-spacing: 1px;
  }
  .tiger-artwork {
    position: absolute;
    left: 305px;
    top: 452px;
    width: 590px;
    height: 440px;
    border-radius: 46% 46% 40% 40% / 38% 38% 55% 55%;
    background: radial-gradient(ellipse at 50% 55%, var(--brand-cream) 0%, var(--brand-peach) 45%, var(--brand-orange) 85%, rgba(243,113,35,0) 100%);
  }
  .abv {
    position: absolute;
    left: 1020px;
    top: 570px;
    transform: translate(-50%, -50%) rotate(-90deg);
    font-family: "Arimo", sans-serif;
    font-size: 28px;
    color: var(--brand-yellow);
    white-space: nowrap;
    letter-spacing: 1px;
  }
</style>
</head>
<body>
<div class="label">
  <svg class="label-frame" width="1200" height="1000" viewBox="0 0 1200 1000" aria-hidden="true">
    <defs>
      <linearGradient id="frame-band" x1="0" y1="0" x2="1" y2="0">
        <stop offset="0" stop-color="#f37123"/>
        <stop offset="0.3" stop-color="#f8ba93"/>
        <stop offset="0.55" stop-color="#fbed22"/>
        <stop offset="0.8" stop-color="#f8ba93"/>
        <stop offset="1" stop-color="#f37123"/>
      </linearGradient>
    </defs>
    <polygon class="frame-outer" fill="url(#frame-band)" stroke="#000" stroke-width="6"
      points="165,38 1035,38 1035,72 1075,72 1075,116 1115,116 1115,882 1075,882 1075,926 1035,926 1035,960 165,960 165,926 125,926 125,882 85,882 85,116 125,116 125,72 165,72"/>
    <polygon class="frame-line" fill="#fbed22" stroke="#000" stroke-width="2"
      points="185,58 1015,58 1015,92 1055,92 1055,136 1095,136 1095,862 1055,862 1055,906 1015,906 1015,940 185,940 185,906 145,906 145,862 105,862 105,136 145,136 145,92 185,92"/>
    <polygon class="frame-field" fill="#000"
      points="195,68 1005,68 1005,102 1045,102 1045,146 1085,146 1085,852 1045,852 1045,896 1005,896 1005,930 195,930 195,896 155,896 155,852 115,852 115,146 155,146 155,102 195,102"/>
  </svg>

  <div class="crest-ornament" role="img" aria-label="Gold crown flourish ornament"></div>

  <h1 class="brand-name">Mango Spin</h1>
  <span class="registered-mark">®</span>

  <div class="tagline-rule top"></div>
  <p class="tagline">Pure Tequila</p>
  <div class="tagline-rule bottom"></div>

  <div class="tiger-artwork" role="img" aria-label="Illustration of a snarling tiger head in orange and gold tones"></div>

  <div class="abv">Alc .cc. 40%</div>
</div>
</body>
</html>
```